Scrubbing Paper Towel Company needs Label Design

We need a product label that wraps around a roll of scrubbing paper towels as a sticker label of individually wrapped rolls. The sticker label has dimensions of 11.5" x 6" (width x height). The company logo with the brand feel and color theme is attached.

This is mainly used for dishwashing. A very large section of the label should show dishwashing and cleaning. Two very similar products can be found here :
---> https://www.shopvarnel.example/Non-Scratch-Disposable-Dish-Washing-Scrubbing-KT47M/dp/Q5283LRTVN/ref=sr_1_9?keywords=scouring+sheet&qid=2840175396&sr=8-9
--->https://www.shopvarnel.example/Zuvi-Flair-Disposable-Dish-washing-Scrubbing/dp/Q3961HWPXT/ref=sr_1_15?keywords=scouring+sheet&qid=2840175396&sr=8-15

To be included in the label:

Key points:
Did you know? Sponges are the perfect place for bacteria growth! We're talking hundreds of different species of bacteria growing in your dishwashing sponge - just as bad as the inside of your toilet. So why use a dirty sponge over and over again? Why does it smell so bad? Yes your toilet is gross, but why should the sponge go overlooked?

The Brisko Roll is a sanitary solution to this problem. Use it once, wash and reuse up to three times before throwing each sheet away - that's enough for 180 washes per roll! But don't limit yourself to dishwashing. It's great for scrubbing surfaces with hardened debris or even dry residue left from old spills. So go ahead, take a stand against bacteria and wash away knowing your kitchen is finally clean. Now that's sanitary!

Multipurpose Use:
Dishwashing
**(with example image/graphic)**
Cleaning Toilets
Cleaning Grills
Wiping Down Stoves
Cleaning Sinks
Cleaning Pet Bowls

60 Sheets
7.9" X 8.7" per sheet

Features:
Perforated for Easy Tear
Reusable
Liquid Absorbent
Non-Flammable
Cadmium Free
Kitchen Safe

```html
<!DOCTYPE html>
<html lang="en">
<head>
<meta charset="utf-8">
<title>Brisko Roll – Wrap Label</title>
<link href="https://fonts.googleapis.com/css2?family=EB+Garamond:wght@400;500&family=Montserrat:wght@600;700;800&display=swap" rel="stylesheet">
<style>
  :root {
    --page: #efc96c;
    --label-cream: #f4df9f;
    --label-branch: #f5cc5c;
    --panel-blue: #283a8f;
    --hero-blue: #2b3c9e;
    --white: #ffffff;
    --serif: "EB Garamond", Georgia, serif;
    --sans: "Montserrat", Arial, sans-serif;
  }
  * { box-sizing: border-box; margin: 0; padding: 0; }
  html, body { width: 857px; height: 1200px; overflow: hidden; }
  body { background: var(--page); position: relative; }

  .wrap-label {
    position: absolute; left: 0; top: 377px;
    width: 857px; height: 446px;
    background: var(--label-cream);
    overflow: hidden;
  }
  .branch-pattern {
    position: absolute; inset: 0;
    background: radial-gradient(ellipse at 30% 40%, var(--label-branch) 0%, var(--label-cream) 70%);
  }

  .info-panel {
    position: absolute; top: 47px; width: 126px; height: 356px;
    background: var(--panel-blue); color: var(--white);
    font-family: var(--serif); text-align: center;
  }
  .story-panel { left: 30px; padding: 14px 8px 0; }
  .feature-panel { left: 703px; padding: 9px 6px 0; }

  .mini-brand {
    font-family: var(--sans); font-weight: 800; font-size: 15px;
    line-height: 1; display: flex; align-items: center; justify-content: center; gap: 4px;
    margin-bottom: 2px;
  }
  .mini-brand .dot { width: 7px; height: 7px; border-radius: 50%; background: var(--white); }
  .mini-tagline { font-family: var(--sans); font-weight: 600; font-size: 4.5px; margin-bottom: 16px; }

  .story-text { font-size: 7.1px; line-height: 9.8px; }
  .story-text + .story-text { margin-top: 9px; }

  .feature-list { list-style: none; font-size: 8.3px; line-height: 12px; }
  .feature-list li::before { content: "•"; margin-right: 5px; }
  .use-intro { font-size: 8px; line-height: 11px; margin: 10px 0 7px; }
  .use-list { list-style: none; }
  .use-item {
    display: flex; align-items: center; height: 33px; font-size: 8px;
  }
  .use-item svg { width: 26px; height: 26px; margin-left: 8px; flex: none; }
  .use-item span { flex: 1; text-align: center; }

  .hero-panel {
    position: absolute; left: 307px; top: 0; width: 228px; height: 446px;
    background: var(--hero-blue); color: var(--white);
    text-align: center; font-family: var(--sans);
  }
  .hero-kicker { font-weight: 700; font-size: 9px; line-height: 12px; margin-top: 28px; letter-spacing: .2px; }
  .hero-brand { margin-top: 92px; font-weight: 800; line-height: .95; display: flex; flex-direction: column; align-items: center; }
  .hero-brand .name { font-size: 56px; display: flex; align-items: center; gap: 8px; }
  .hero-brand .dot { width: 18px; height: 18px; border-radius: 50%; background: var(--white); }
  .hero-brand .sub { font-size: 40px; margin-top: 4px; }
  .hero-tagline { font-weight: 600; font-size: 11px; margin-top: 10px; }
  .sheet-count { position: absolute; left: 0; right: 0; top: 360px; font-weight: 800; font-size: 31px; line-height: 1; }
  .sheet-meta { position: absolute; left: 0; right: 0; top: 395px; font-weight: 600; font-size: 6.4px; line-height: 10px; }
</style>
</head>
<body>
<section class="wrap-label">
  <div class="branch-pattern" role="img" aria-label="Pale yellow background with a pattern of golden branching lines"></div>

  <article class="info-panel story-panel">
    <div class="mini-brand"><span class="dot"></span>Brisko Roll</div>
    <div class="mini-tagline">Clean Smarter, Not Harder</div>
    <p class="story-text">Common cleaning sponges are the perfect place for bacteria growth! We're talking hundreds of different species of bacteria growing in your dishwashing sponge - just as bad as the inside of your toilet. So why use a dirty sponge over and over again? Why does it smell so bad? Yes your toilet is gross, but why should the sponge go overlooked?</p>
    <p class="story-text">The Brisko Roll is a sanitary solution to this problem. Use it once, wash and reuse up to three times before throwing each sheet away - that's enough for 180 washes per roll! But don't limit yourself to dishwashing. It's great for scrubbing surfaces with hardened debris or even dry residue left from old spills. So go ahead, take a stand against bacteria and wash away knowing your kitchen is finally clean. Now that's sanitary!</p>
  </article>

  <article class="hero-panel">
    <p class="hero-kicker">SCRUBBING PAPER TOWELS<br>FOR SANITARY CLEANING</p>
    <div class="hero-brand">
      <span class="name"><span class="dot"></span>Brisko</span>
      <span class="sub">ROLL</span>
    </div>
    <p class="hero-tagline">Clean Smarter, Not Harder</p>
    <p class="sheet-count">60</p>
    <p class="sheet-meta">REUSEABLE<br>7.9" X 8.7" SHEETS</p>
  </article>

  <article class="info-panel feature-panel">
    <ul class="feature-list">
      <li>Perforated for Easy Tear</li>
      <li>Reusable</li>
      <li>Liquid Absorbent</li>
      <li>Non-Flammable</li>
      <li>Cadmium Free</li>
      <li>Kitchen Safe</li>
    </ul>
    <p class="use-intro">Suitable for all kinds of cleaning areas, for example:</p>
    <ul class="use-list">
      <li class="use-item">
        <svg viewBox="0 0 26 26" fill="none" stroke="#fff" stroke-width="1.2"><rect x="2" y="2" width="6" height="5"/><rect x="11" y="2" width="5" height="5"/><rect x="19" y="2" width="5" height="5"/><rect x="2" y="12" width="22" height="12"/><line x1="13" y1="12" x2="13" y2="24"/><line x1="2" y1="16" x2="24" y2="16"/></svg>
        <span>Kitchen</span></li>
      <li class="use-item">
        <svg viewBox="0 0 26 26" fill="none" stroke="#fff" stroke-width="1.2"><circle cx="13" cy="13" r="11"/><circle cx="13" cy="13" r="7"/><path d="M10 20v-8M13 20v-9M16 20v-8"/></svg>
        <span>Dishwashing</span></li>
      <li class="use-item">
        <svg viewBox="0 0 26 26" fill="none" stroke="#fff" stroke-width="1.2"><rect x="2" y="4" width="22" height="18"/><circle cx="8.5" cy="11" r="3.5"/><circle cx="17.5" cy="11" r="3.5"/><line x1="6" y1="18" x2="20" y2="18"/></svg>
        <span>Gas Stove</span></li>
      <li class="use-item">
        <svg viewBox="0 0 26 26" fill="none" stroke="#fff" stroke-width="1.2"><path d="M10 2q-2 2 0 4M13 2q-2 2 0 4M16 2q-2 2 0 4"/><circle cx="13" cy="16" r="8"/><line x1="5" y1="16" x2="21" y2="16"/><line x1="6" y1="12.5" x2="20" y2="12.5"/><line x1="6" y1="19.5" x2="20" y2="19.5"/></svg>
        <span>Grill</span></li>
      <li class="use-item">
        <svg viewBox="0 0 26 26" fill="none" stroke="#fff" stroke-width="1.2"><rect x="4" y="2" width="8" height="9"/><path d="M4 11h18q0 7-8 8v5H8v-5q-4-2-4-8z"/></svg>
        <span>Toilet</span></li>
      <li class="use-item">
        <svg viewBox="0 0 26 26" fill="none" stroke="#fff" stroke-width="1.2"><path d="M6 13V5q0-3 3-3t3 3"/><path d="M2 13h22v4q0 5-5 5H7q-5 0-5-5z"/><line x1="7" y1="22" x2="6" y2="25"/><line x1="19" y1="22" x2="20" y2="25"/></svg>
        <span>Bathroom</span></li>
      <li class="use-item">
        <svg viewBox="0 0 26 26" fill="none" stroke="#fff" stroke-width="1.2"><rect x="1" y="7" width="24" height="13" rx="6"/><ellipse cx="8" cy="13" rx="4" ry="3"/><ellipse cx="18" cy="13" rx="4" ry="3"/></svg>
        <span>Pet bowls</span></li>
    </ul>
  </article>
</section>
</body>
</html>
```